Professional DJ Business Card

Business card for giving out to clubs and venues or interested groups that are in need of a professional DJ. I want something artistic and catchy/alluring, with a minimalist approach that gets just the vital amount of info and leaves the rest for inquiry via contacting me. Ideally I would like one side to have an image of something cool like an eye and my name, then the other side be the contact info, I am definitely feeling a black or dark colored card, but I am open to other designs. I am uploading a picture that I made that reflects a little of what I am *kind of* looking for.

Industry/Entity Type

Business

Contact Information for Business Card

Tomas Halvik (Voxtel)
Professional DJ (West Coast)
EDM (Deep/House/Techno), Hip Hop, Latin, Trap.
Cell: 555-274-9163
Email: Voxtelofficial@mailnest.net
www.beatcloudia.net/yourtuneisfading

```html
<!DOCTYPE html>
<html lang="en">
<head>
<meta charset="UTF-8">
<title>Voxtel – DJ Business Card</title>
<link rel="stylesheet" href="https://fonts.googleapis.com/css2?family=Open+Sans:wght@400&display=swap">
<style>
  :root {
    --backdrop: #e6e3df;
    --card: #111312;
    --ink: #f2f2f0;
    --ink-soft: #e4e4e2;
    --rule: #c9c9c7;
  }
  * { box-sizing: border-box; margin: 0; padding: 0; }
  html, body {
    width: 1189px; height: 1200px; overflow: hidden;
    background: var(--backdrop);
    font-family: "Open Sans", sans-serif;
  }
  .canvas { position: relative; width: 1189px; height: 1200px; }
  .card {
    position: absolute; left: 140px; width: 918px; height: 522px;
    background: var(--card);
  }
  .card--front { top: 47px; }
  .card--back { top: 624px; }

  .wordmark {
    position: absolute; transform: translate(-50%, -50%);
    display: flex; align-items: center; gap: 22px;
    color: var(--ink); font-size: 108px; font-weight: 400; letter-spacing: 2px;
    line-height: 1; white-space: nowrap;
  }
  .wordmark__dot {
    width: 30px; height: 30px; border-radius: 50%; background: var(--ink); flex: none;
  }
  .card--front .wordmark { left: 458px; top: 150px; }
  .card--back .wordmark { left: 614px; top: 330px; }

  .divider {
    position: absolute; left: 0; right: 0; top: 297px;
    height: 1px; background: var(--rule);
  }
  .identity {
    position: absolute; left: 39px; top: 334px; color: var(--ink-soft);
  }
  .identity__name {
    font-size: 32px; line-height: 44px; font-weight: 400; color: var(--ink);
  }
  .identity__detail { font-size: 23.5px; line-height: 30px; margin-top: 6px; }

  .contacts {
    position: absolute; right: 46px; top: 382px; list-style: none;
    color: var(--ink-soft); font-size: 23.5px; line-height: 30px;
  }
  .contacts li {
    display: flex; align-items: center; justify-content: flex-end; gap: 14px;
    height: 31px;
  }
  .contacts svg { width: 19px; height: 19px; flex: none; }
</style>
</head>
<body>
<div class="canvas">
  <section class="card card--front">
    <div class="wordmark"><span class="wordmark__dot"></span>Voxtel</div>
    <div class="divider"></div>
    <div class="identity">
      <h1 class="identity__name">Tomas Halvik (Voxtel)</h1>
      <p class="identity__detail">Professional DJ (West Coast)<br>EDM (Deep/House/Techno),<br>Hip Hop, Latin, Trap.</p>
    </div>
    <ul class="contacts">
      <li>555-274-9163
        <svg viewBox="0 0 20 20" aria-hidden="true"><rect width="20" height="20" rx="2" fill="#f2f2f0"/><path d="M6 4.5c1 0 1.6.5 1.8 1.5l.4 1.6c.1.6-.3 1-.8 1.2.6 1.6 1.5 2.6 2.9 3.4.3-.5.7-.8 1.3-.6l1.5.6c.8.4 1 1 .7 1.8-.5 1.3-1.6 1.8-2.9 1.3-3.2-1.3-5.3-3.6-6.2-7.2C4.4 5.7 4.9 4.6 6 4.5z" fill="#111312"/></svg>
      </li>
      <li>Voxtelofficial@mailnest.net
        <svg viewBox="0 0 20 20" aria-hidden="true"><rect width="20" height="20" rx="2" fill="#f2f2f0"/><rect x="3.5" y="6" width="13" height="8.5" fill="none" stroke="#111312" stroke-width="1.5"/><path d="M3.5 6l6.5 5 6.5-5" fill="none" stroke="#111312" stroke-width="1.5"/></svg>
      </li>
      <li>www.beatcloudia.net/yourtuneisfading
        <svg viewBox="0 0 20 20" aria-hidden="true"><rect width="20" height="20" rx="2" fill="#f2f2f0"/><circle cx="10" cy="10" r="6" fill="none" stroke="#111312" stroke-width="1.5"/><path d="M4 10h12M10 4c-2.2 2-2.2 10 0 12M10 4c2.2 2 2.2 10 0 12" fill="none" stroke="#111312" stroke-width="1.2"/></svg>
      </li>
    </ul>
  </section>

  <section class="card card--back">
    <div class="wordmark"><span class="wordmark__dot"></span>Voxtel</div>
  </section>
</div>
</body>
</html>
```